Gestaltung Flyer & Infokärtchen für Tellerbund
Zielgruppe
Hungrige Personen im Geschäft/Firma (keine Privatpersonen zu Hause), welche Menüs bestellen wollen. Die Menüs dürfen nicht zuviel kosten, aber der Flyer darf deshalb auch nicht "billig" daher kommen. Im Gegenteil.
Aufgabenstellung
Tellerbund - Deine Food Community ist eine seite, die virtuelle Bestellgemeinschaften schafft und damit Lieferpauschalen und Mindestbestellmengen für den Einzelbesteller umgeht. Der Einzelbesteller kennt also seine "Mitbesteller" nicht. Zudem wird das Menü günstiger, je mehr Leute in seiner Community bestellen. Diese Mitbesteller sind andere Personen in der gleichen Firma oder direkte Nachbarfirmen. In jedem Fall geht es um Bestellung von warmen Menüs.
Enorm wichtig und absolut zentral bei dem Infoflyer A4 UND dem kleinen Infokärtchen (A6 gefaltet mit aussen hinten weiss, aussen vorne Hauptmessage mit Logo (seperater Wettbewerb) und Innen zentrale Messages mit Internetseite www.TBM.ch) ist:
1. Der zentrale Unterschied zu anderen Bestellsystemen. warum der Kunde bei uns bestellen soll. Aus 2 Gründen!
1. "Keine Lieferpauschale", "Keine Mindestbestellmenge", "Punkte sammeln". Keine Lieferpauschale und keine Mindestbestellmenge - auch wenn nur 1 Menü bestellt wird. Bei Jedem Kauf kann der Besteller Punkte sammeln und diese dann in gratis Menü umwandeln. Zudem sammelt auch die virtuelle Bestellgemeinschaft punkte. Bei Erreichen von xy Punkten wird in der Community Preise verlost.
2. Community Gedanke: Je mehr bestellt wird, desto günstiger wird der Preis - bis zu einem bestimmten Minimum. Bei ersten Besteller kostet also bspw. das Menü warm geliefert all inkl. 15 Euro; bis minimum 9 Euro. Es muss aber voraus bezahlt werden (diese info muss aber ncht unbedingt auch drauf).
Beispiele für den Community Gedanken wären:
- "Tellerbund - Deine Food Community - Je mehr bestellen, desto günstiger wird’s"
- "Tellerbund - Deine Food Community - Andere bestellen - Du profitierst"
- "Tellerbund - Deine Food Community - Du bist teil der Community - mehr Besteller - günstiger Preis" etc.
- oder man stellt dies bildlich dar zusammen bspw. mit text 1 (ich stelle mir bspw. vor, 1 männchen hoher Preis ($ oben auf berg) und..

```html
<!DOCTYPE html>
<html lang="de">
<head>
<meta charset="utf-8">
<title>Tellerbund – Flyer</title>
<link rel="stylesheet" href="https://fonts.googleapis.com/css2?family=Arimo:wght@400;700&family=Schoolbell&display=swap">
<style>
  :root {
    --page: #ffffff;
    --sky-top: #eef4f8;
    --sky-mid: #d6e6f1;
    --sky-low: #e9f1f6;
    --mint: #e3efd6;
    --note: #dcedc4;
    --note-edge: #c9dfae;
    --ink-red: #c8312a;
    --blue: #4588c6;
    --blue-dark: #2f6ea8;
    --green: #a9c95a;
    --green-dark: #7fa53a;
    --green-light: #c3dc82;
    --napkin: #f1f1ef;
    --napkin-shade: #d9d9d6;
    --food-a: #e9d9a8;
    --food-b: #c86a3c;
    --food-c: #6f9c48;
    --white: #ffffff;
    --grey: #8a8f94;
  }
  html, body {
    margin: 0;
    width: 1200px;
    height: 1200px;
    overflow: hidden;
    background: var(--page);
  }
  .flyer {
    position: absolute;
    left: 223px;
    top: 50px;
    width: 755px;
    height: 1068px;
    overflow: hidden;
    background: linear-gradient(180deg, var(--sky-top) 0%, var(--sky-mid) 55%, var(--sky-low) 100%);
    box-shadow: 2px 3px 10px rgba(0,0,0,0.25);
    font-family: "Arimo", Arial, sans-serif;
  }
  .flyer-shapes {
    position: absolute;
    inset: 0;
  }
  .note {
    position: absolute;
    left: 95px;
    top: 40px;
    width: 285px;
    height: 265px;
    background: var(--note);
    border-bottom: 3px solid var(--note-edge);
    transform: rotate(2deg);
    box-shadow: 1px 3px 6px rgba(0,0,0,0.15);
    padding: 38px 18px 0 22px;
    box-sizing: border-box;
  }
  .note-list {
    list-style: none;
    margin: 0;
    padding: 0;
    font-family: "Schoolbell", cursive;
    color: var(--ink-red);
    font-size: 23px;
    line-height: 1.05;
    transform: rotate(6deg);
    transform-origin: left top;
  }
  .note-list li { margin-bottom: 16px; }
  .napkin {
    position: absolute;
    left: 410px;
    top: -10px;
    width: 360px;
    height: 355px;
    background: linear-gradient(160deg, var(--napkin) 0%, #fafaf9 45%, var(--napkin-shade) 100%);
    transform: rotate(6deg);
    box-shadow: -2px 4px 8px rgba(0,0,0,0.18);
  }
  .brand {
    position: absolute;
    left: 470px;
    top: 120px;
    display: flex;
    align-items: center;
    gap: 12px;
  }
  .brand-dot {
    width: 30px;
    height: 30px;
    border-radius: 50%;
    background: var(--green);
  }
  .brand-name {
    font-weight: 700;
    font-size: 34px;
    color: var(--grey);
    letter-spacing: 0.5px;
  }
  .headline {
    position: absolute;
    left: 60px;
    top: 395px;
    margin: 0;
    font-weight: 700;
    font-size: 84px;
    line-height: 1;
    color: var(--blue);
    -webkit-text-stroke: 0;
    text-shadow:
      3px 0 0 var(--white), -3px 0 0 var(--white), 0 3px 0 var(--white), 0 -3px 0 var(--white),
      2px 2px 0 var(--white), -2px -2px 0 var(--white), 2px -2px 0 var(--white), -2px 2px 0 var(--white),
      3px 5px 6px rgba(0,0,0,0.25);
  }
  .headline-line { display: block; }
  .headline-line.second { margin: 14px 0 0 88px; }
  .cta {
    position: absolute;
    left: 262px;
    top: 620px;
    width: 240px;
    height: 62px;
    border-radius: 9px;
    background: linear-gradient(180deg, var(--green-light) 0%, var(--green) 55%, var(--green-dark) 100%);
    border: 3px solid var(--white);
    box-shadow: 1px 3px 5px rgba(0,0,0,0.25);
    color: var(--white);
    font-size: 27px;
    font-weight: 400;
    display: flex;
    align-items: center;
    justify-content: center;
    box-sizing: border-box;
  }
  .cta-pointer {
    position: absolute;
    left: 420px;
    top: 668px;
    width: 40px;
    height: 56px;
  }
  .dish {
    position: absolute;
    left: -20px;
    top: 760px;
    width: 470px;
    height: 235px;
    border-radius: 50% / 48%;
    background: radial-gradient(ellipse at 45% 50%, var(--food-a) 0%, var(--food-b) 45%, var(--food-c) 75%, #f4f1e8 92%);
  }
  .site {
    position: absolute;
    left: 50px;
    top: 1012px;
    color: var(--white);
    font-weight: 700;
    font-size: 25px;
  }
</style>
</head>
<body>
  <main class="flyer">
    <svg class="flyer-shapes" width="755" height="1068" viewBox="0 0 755 1068" aria-hidden="true">
      <defs>
        <linearGradient id="mintFade" x1="0" y1="0" x2="0" y2="1">
          <stop offset="0" stop-color="#e3efd6"/>
          <stop offset="1" stop-color="#e3efd6" stop-opacity="0"/>
        </linearGradient>
        <linearGradient id="bandGreen" x1="0" y1="0" x2="0" y2="1">
          <stop offset="0" stop-color="#c3dc82"/>
          <stop offset="1" stop-color="#a9c95a"/>
        </linearGradient>
      </defs>
      <rect x="0" y="0" width="755" height="330" fill="url(#mintFade)"/>
      <circle cx="720" cy="560" r="380" fill="#ffffff" fill-opacity="0.22"/>
      <circle cx="720" cy="560" r="300" fill="#ffffff" fill-opacity="0.15"/>
      <path d="M0 900 C 220 1010, 480 960, 755 870 L755 1068 L0 1068 Z" fill="url(#bandGreen)"/>
    </svg>

    <div class="napkin" role="img" aria-label="Gefaltete Stoffserviette"></div>
    <div class="brand">
      <span class="brand-dot"></span>
      <span class="brand-name">TELLERBUND</span>
    </div>

    <div class="note">
      <ul class="note-list">
        <li>– Keine Mindestbestellung</li>
        <li>– Keine Lieferpauschal</li>
        <li>–Essen und Punkte<br>&nbsp;sammeln</li>
      </ul>
    </div>

    <h1 class="headline">
      <span class="headline-line">Schlemmen</span>
      <span class="headline-line second">und Punkten</span>
    </h1>

    <div class="cta">jetzt sparen</div>
    <svg class="cta-pointer" viewBox="0 0 20 28" aria-hidden="true">
      <path d="M1 1 L1 21 L6 16 L10 26 L13 25 L9 15 L16 15 Z" fill="#ffffff" stroke="#333" stroke-width="1.2" stroke-linejoin="round"/>
    </svg>

    <div class="dish" role="img" aria-label="Teller mit Pasta, Tomaten und Spinat"></div>

    <svg class="flyer-shapes" width="755" height="1068" viewBox="0 0 755 1068" role="img" aria-label="Schwarm aus Mauszeigern">
      <defs>
        <linearGradient id="swarm" x1="1" y1="0" x2="0" y2="1">
          <stop offset="0" stop-color="#ffffff" stop-opacity="0.9"/>
          <stop offset="1" stop-color="#e6e8ea" stop-opacity="0.95"/>
        </linearGradient>
      </defs>
      <path d="M755 790 L755 1068 L350 1068 C 420 1030, 520 960, 600 880 C 660 830, 720 800, 755 790 Z" fill="url(#swarm)"/>
    </svg>

    <div class="site">www.tellerbund.ch</div>
  </main>
</body>
</html>
```